Yacht Management in Miami & Ft Lauderdale (2019Q2)

I’m looking for a flyer to leave places for people to get information about my company and what services we offer.
We offer monthly management plans to ensure the vessel is ready to go at a moments notice. This can be as simple as washing once a week, or as involved as washing, waxing, detailing, provisioning, and crew services.
We also offer bespoke customizations; stereos, on board WiFi, and engineering.

Target Market(s)

Yacht and boat owners.

Font styles to use
Sans Serif

Colors
87d0c7
85cae6
85acd3
cedeed
cee9f5
cfeae6
0455a3

Requirements
Must have
• Must have simple attention grabbing, without being obnoxious.
• Prefer a 3in x 5in post card size. other size may be an option.
• Must be front and back.
Nice to have
• Languages: English, Spanish, Russian
• USA flag logo
Should not have
• Should not have a lot of text. Icons and photos are great.

```html
<!DOCTYPE html>
<html lang="en">
<head>
<meta charset="utf-8">
<title>Harbor Keepers – Yacht Management Flyer</title>
<link href="https://fonts.googleapis.com/css2?family=Montserrat:wght@400;500;700&display=swap" rel="stylesheet">
<style>
  :root {
    --ink: #000000;
    --paper: #ffffff;
    --accent: #ed1c24;
    --rule: #bfbfbf;
    --hull-light: #e4e6e8;
    --hull-mid: #9ea4aa;
    --hull-blue: #4f7596;
    --sea: #1a9fd6;
  }
  * { box-sizing: border-box; margin: 0; padding: 0; }
  html, body { width: 849px; height: 1200px; overflow: hidden; background: var(--ink); }
  .flyer {
    position: relative; width: 849px; height: 1200px; overflow: hidden;
    background: var(--ink); color: var(--paper);
    font-family: "Montserrat", sans-serif;
  }
  .brand {
    position: absolute; left: 104px; top: 96px; width: 232px; height: 360px;
    display: flex; flex-direction: column; align-items: center; justify-content: center; gap: 22px;
  }
  .brand-dot { width: 70px; height: 70px; border-radius: 50%; background: var(--paper); }
  .brand-name {
    font-weight: 700; font-size: 38px; line-height: 1.05; text-align: center;
    color: var(--paper); letter-spacing: 1px;
  }
  .about {
    position: absolute; left: 542px; top: 174px; width: 229px; height: 207px;
    border-top: 1px solid var(--rule); border-bottom: 1px solid var(--rule);
  }
  .section-title {
    font-weight: 400; font-size: 26px; letter-spacing: 0.3px; line-height: 1;
  }
  .section-title strong { font-weight: 700; }
  .about .section-title { color: var(--accent); text-align: right; margin-top: 36px; }
  .about-text {
    margin-top: 12px; font-size: 16.5px; line-height: 20.6px; text-align: justify;
  }
  .services {
    position: absolute; left: 0; top: 543px; width: 504px; height: 328px;
    background: var(--accent); padding: 23px 0 0 77px;
  }
  .services .section-title { color: var(--paper); }
  .service-list { list-style: none; margin-top: 21px; width: 380px; }
  .service-list li {
    position: relative; padding-left: 32px; font-size: 16.8px; line-height: 20.6px;
    margin-bottom: 10px;
  }
  .service-list li::before {
    content: ""; position: absolute; left: 0; top: 0; bottom: 0; width: 8px; background: var(--ink);
  }
  .contact { position: absolute; left: 542px; top: 563px; width: 229px; text-align: right; }
  .contact .section-title { color: var(--accent); }
  .contact-label {
    display: flex; justify-content: flex-end; align-items: center; gap: 8px;
    color: var(--accent); font-size: 17px; height: 30px; border-bottom: 1px solid var(--rule);
  }
  .contact-label svg { fill: var(--paper); }
  .label-location { margin-top: 112px; }
  .contact-value { font-size: 16.5px; line-height: 20.6px; padding: 9px 0 4px; }
  .address { border-bottom: 1px solid var(--rule); padding-bottom: 5px; margin-bottom: 12px; }
  .yacht-art {
    position: absolute; left: 56px; top: 960px; width: 793px; height: 240px;
    background: linear-gradient(180deg, var(--hull-light) 0%, var(--hull-mid) 55%, var(--hull-blue) 78%, var(--sea) 100%);
    border-radius: 120px 40px 0 0;
  }
</style>
</head>
<body>
<main class="flyer">
  <div class="brand">
    <span class="brand-dot"></span>
    <div class="brand-name">HARBOR<br>KEEPERS</div>
  </div>

  <section class="about">
    <h2 class="section-title">ABOUT <strong>US</strong></h2>
    <p class="about-text">We perform most projects in-house, but when we use sub-contractors, we only use the best. Yes, there are some in Florida.</p>
  </section>

  <section class="services">
    <h2 class="section-title">OUR <strong>SERVICES</strong></h2>
    <ul class="service-list">
      <li>Harbor Keepers are here to refit and update your yacht.</li>
      <li>We offer monthly management plans to ensure the vessel is ready to go at a moments notice</li>
      <li>This can be as simple as washing once a week, or as involved as washing, waxing, detailing, provisioning, and crew services.</li>
      <li>We also offer bespoke customizations; stereos, on board WiFi, and engineering.</li>
    </ul>
  </section>

  <section class="contact">
    <h2 class="section-title">CONTACT <strong>US</strong></h2>
    <div class="contact-label label-location">LOCATION
      <svg width="12" height="16" viewBox="0 0 12 16" aria-hidden="true"><path d="M6 0C2.7 0 0 2.6 0 5.9 0 10.3 6 16 6 16s6-5.7 6-10.1C12 2.6 9.3 0 6 0zm0 8.2A2.3 2.3 0 1 1 6 3.6a2.3 2.3 0 0 1 0 4.6z"/></svg>
    </div>
    <p class="contact-value address">480 Coral Way, #210<br>Miami Beach, FL 33140</p>
    <div class="contact-label">MOBILE
      <svg width="10" height="16" viewBox="0 0 10 16" aria-hidden="true"><path d="M2 0h6a2 2 0 0 1 2 2v12a2 2 0 0 1-2 2H2a2 2 0 0 1-2-2V2a2 2 0 0 1 2-2zm0 2v11h6V2z"/></svg>
    </div>
    <p class="contact-value">(954) 555-0172</p>
  </section>

  <div class="yacht-art" role="img" aria-label="Illustration of a white motor yacht with a blue hull on the water"></div>
</main>
</body>
</html>
```